New look modernised front page for Marlowe Lawn Sports Guild Website Which incorporates our new logo (to be provided as a png file)
We want the home page to a panel to allow an image rotator and provide ready access to links to other inflation via some link menus/panel/button
1. Join a Croquet Club - links to details about Croquet in NSW - gateway to information of interest or the general public/“interested others” eg about the game, clubs locations and contacts
2. Club and Member Information - newsletters, Calender of events, and downloads
3. Officials and volunteers - training resources etc
4. Member and Club sign in - access to database
5. About Us - information about Marlowe Lawn Sports Guild incorporated -peak body for croquet in NSW - governance, contact details etc

Current website is at https://www.marlowe-guild.org/index.html

Target Market(s)

Dual target - People interested in learning about croquet and existing members

Number of Pages Required

1 page

Font styles to use
Sans Serif

Colors
0255a3
3377b5
85acd3
85cae6
33a6d7
0792cd
00a990

Requirements
Must have
• Contemporary feel
• Include logo - file attached
• Colours to include blues which are the NSW colour
Nice to have
• We want the home page to a panel to allow an image rotator and provide ready access to links to other inflation via some link menus/panel/button
• 1. Join a Croquet Club - links to details about Croquet in NSW - gateway to information of interest or the general public/“interested others” eg about the game, clubs locations and contacts
• 2. Club and Member Information - newsletters, Calender of events, and downloads
• 3. Officials and volunteers - training resources etc
• 4. Member and Club sign in - access to database
• 5. About Us - information about Marlowe Lawn Sports Guild incorporated -peak body for croquet in NSW - governance, contact details etc
• Want to have feeling of activity/movement/alive
• Current website is at https://www.marlowe-guild.org/index.html
• Some photos attached for information

```html
<!DOCTYPE html>
<html lang="en">
<head>
<meta charset="utf-8">
<title>Marlowe Lawn Sports Guild</title>
<link href="https://fonts.googleapis.com/css2?family=Roboto:wght@400;500;700&family=Roboto+Condensed:wght@400;700&display=swap" rel="stylesheet">
<style>
:root{
  --navy:#0255a3;
  --blue:#3377b5;
  --blue-soft:#85acd3;
  --sky:#85cae6;
  --cyan:#33a6d7;
  --azure:#0792cd;
  --green:#00a990;
  --ink:#1d2b4a;
  --text:#6a7280;
  --footer:#0c1526;
  --pale:#eef3fa;
}
*{box-sizing:border-box;margin:0;padding:0}
html,body{width:1200px;height:4018px;overflow:hidden;background:#fff}
body{font-family:"Roboto",sans-serif;color:var(--text)}
.page{position:relative;width:1200px;height:4018px;overflow:hidden}
.abs{position:absolute}
.head{font-family:"Roboto Condensed","Roboto",sans-serif;font-weight:700;text-transform:uppercase}
.ghost{position:absolute;font-family:"Roboto Condensed",sans-serif;font-weight:700;text-transform:uppercase;color:rgba(2,85,163,.07);white-space:nowrap}
.btn{position:absolute;display:flex;align-items:center;justify-content:center;border-radius:30px;font-size:15px;font-weight:500;text-decoration:none}
.btn-outline-green{border:2px solid var(--green);color:var(--green);background:#fff}
.btn-green{background:var(--green);color:#fff}

/* top bar */
.topline{left:0;top:0;width:1200px;height:5px;background:var(--navy)}
.tab{top:0;height:38px;color:#fff;font-size:13px;font-weight:700;display:flex;align-items:center;justify-content:center;gap:8px;text-transform:uppercase}
.tab-member{left:620px;width:205px;background:var(--navy);clip-path:polygon(0 0,100% 0,94% 100%,6% 100%)}
.tab-club{left:885px;width:215px;background:var(--green);clip-path:polygon(0 0,100% 0,94% 100%,6% 100%)}
.state-mark{left:852px;top:6px;width:28px;height:28px;border-radius:50%;background:#fff;border:3px solid var(--navy)}
.header{left:0;top:0;width:1200px;height:130px;background:#fff}
.nav{left:398px;top:78px;display:flex;gap:26px;font-size:15px;color:#333}
.nav a{color:#333;text-decoration:none}
.nav .more{color:var(--navy);text-decoration:underline;font-weight:500}
.logo-disc{left:100px;top:26px;width:228px;height:228px;border-radius:50%;background:#fff;z-index:3;display:flex;flex-direction:column;align-items:center;justify-content:center;text-align:center;padding:0 28px;gap:10px}
.logo-disc .dot{width:34px;height:34px;border-radius:4px;background:var(--navy)}
.logo-disc .name{font-size:21px;font-weight:700;color:var(--navy);line-height:1.15}

/* hero */
.hero{left:0;top:130px;width:1200px;height:598px;background:linear-gradient(180deg,#4f7a3a 0%,#3a6a2c 45%,#2f5a24 100%)}
.hero-box{left:233px;top:311px;width:726px;height:182px;border:2px solid #fff;background:rgba(20,30,20,.55);text-align:center;color:#fff}
.hero-title{font-size:76px;line-height:1;margin-top:40px;letter-spacing:1px}
.hero-sub{font-size:17px;margin-top:18px}
.hero-join{left:485px;top:504px;width:233px;height:46px;background:var(--green);color:#fff;border:2px solid #fff;text-transform:uppercase;font-size:14px}
.dots{left:556px;top:663px;display:flex;gap:6px}
.dots span{width:13px;height:13px;border-radius:50%;border:2px solid #fff}
.dots span:first-child{background:#fff}
.notch{left:570px;top:708px;width:60px;height:24px;background:#fff;clip-path:polygon(0 100%,50% 0,100% 100%)}

/* about */
.about-title{left:99px;top:870px;font-size:34px;color:var(--ink);line-height:1.35}
.about-title span{color:var(--navy);display:block}
.about-text{left:99px;top:978px;width:430px;font-size:13.5px;line-height:2}
.about-text a{color:var(--navy);text-decoration:none}
.about-frame{left:573px;top:860px;width:493px;height:388px;border:3px solid var(--green)}
.about-photo{left:589px;top:873px;width:509px;height:392px;background:linear-gradient(135deg,#6d8a5a,#9aa77a 50%,#c7b48a)}
.play{left:812px;top:1037px;width:64px;height:64px;border-radius:50%;border:3px solid #fff;background:rgba(0,0,0,.15)}
.read-more{left:99px;top:1208px;width:161px;height:46px}

/* newsletters */
.news{left:0;top:1393px;width:1200px;height:622px;background:var(--pale)}
.section-title{position:absolute;left:0;width:1200px;text-align:center;font-size:32px;color:var(--ink)}
.section-title span{color:var(--navy)}
.section-sub{position:absolute;left:0;width:1200px;text-align:center;font-size:14px}
.nl{width:252px;height:252px;border-radius:50%;border:4px solid var(--green);background:#fff;text-align:center;padding-top:62px}
.nl h4{font-size:15px;color:var(--navy);font-weight:700}
.nl p{font-size:12px;line-height:1.6;margin:8px 40px 0;color:#8a8f99}
.nl .rm{font-size:12px;color:#555;margin-top:10px;display:block}
.nl-date{width:108px;height:108px;border-radius:50%;background:var(--green);color:#fff;border:4px solid #fff;display:flex;flex-direction:column;align-items:center;justify-content:center;font-weight:700;font-size:15px;text-transform:uppercase;line-height:1.3}
.nl-date b{font-size:22px}
.arrow{font-size:30px;color:var(--ink);top:1738px}

/* calendar & events */
.cal-panel{left:0;top:2015px;width:415px;height:578px;background:#fff;border-right:2px solid #e6ebf2;border-top:2px solid #e6ebf2}
.cal-title{left:99px;top:2098px;font-size:22px;color:var(--ink)}
.cal{left:99px;top:2151px;width:249px;box-shadow:0 3px 10px rgba(0,0,0,.25);background:#fff}
.cal-head{height:36px;background:var(--navy);color:#fff;display:flex;justify-content:space-between;align-items:center;padding:0 12px;font-size:14px;font-weight:700}
.cal-grid{display:grid;grid-template-columns:repeat(7,1fr);font-size:10px;text-align:center;color:#333}
.cal-grid .wd{font-size:8px;color:#888;padding:6px 0}
.cal-grid div{padding:9px 0;border-top:1px solid #f0f0f0}
.cal-grid .mute{color:#bbb}
.cal-grid .on{background:var(--navy);color:#fff}
.cal-topics{left:104px;top:2410px;font-size:12px;line-height:1.7}
.cal-topics a{color:var(--navy)}
.events-h{font-size:22px;color:var(--navy);font-weight:500}
.ev-list{width:650px;font-size:14px;line-height:1.9}
.ev-list li{list-style:none;position:relative;padding-left:32px;margin-bottom:14px}
.ev-list li::before{content:"»";position:absolute;left:4px;top:0;color:var(--green);font-weight:700}
.more-events{left:463px;top:2432px;width:132px;height:46px}

/* training */
.train{left:0;top:2593px;width:555px;height:509px;background:linear-gradient(135deg,#1459ad,var(--navy))}
.train-title{left:99px;top:2705px;font-size:32px;color:#fff}
.train-text{left:99px;top:2793px;width:420px;font-size:13.5px;line-height:1.95;color:#e6eefa}
.train-btn{left:99px;top:2974px;width:150px;height:45px;border:2px solid #fff;color:#fff}
.train-photo{left:555px;top:2593px;width:645px;height:509px;background:linear-gradient(180deg,#2f4d2a,#4d6b3a 55%,#6d8551)}

/* downloads */
.dl-btn{left:509px;top:3397px;width:182px;height:46px;gap:8px}

/* footer */
.footer{left:0;top:3576px;width:1200px;height:442px;background:var(--footer);border-top:6px solid var(--green)}
.f-logo{left:102px;top:3684px;display:flex;align-items:center;gap:12px;color:#fff;font-size:20px;font-weight:500;white-space:nowrap}
.f-logo .sq{width:28px;height:28px;background:var(--navy);border:2px solid #fff;flex:none}
.f-call{left:102px;top:3762px;color:#fff;font-size:22px;font-weight:700;display:flex;align-items:center;gap:12px}
.f-mid{left:485px;top:3672px;color:#fff;font-size:19px;line-height:1.7;font-weight:500}
.f-contact{left:485px;top:3759px;width:161px;height:48px;border:2px solid #fff;color:#fff;font-size:17px}
.f-news{left:782px;top:3680px;color:#fff;font-size:19px;font-weight:500;text-transform:uppercase}
.f-input{left:782px;top:3742px;width:316px;height:40px;border:1.5px solid #ccd;border-radius:20px;color:#fff;font-size:13px;padding-left:22px;display:flex;align-items:center}
.f-login{left:782px;top:3796px;width:102px;height:38px;background:var(--navy);color:#fff;font-size:14px}
.f-rule{left:102px;top:3932px;width:996px;height:1px;background:rgba(255,255,255,.12)}
.f-copy{left:102px;top:3964px;color:#fff;font-size:13px}
.socials{left:912px;top:3956px;display:flex;gap:14px}
.socials span{width:30px;height:30px;border-radius:50%}
</style>
</head>
<body>
<div class="page">

  <!-- header -->
  <div class="abs header"></div>
  <div class="abs topline"></div>
  <div class="abs tab tab-member">
    <svg width="12" height="12" viewBox="0 0 12 12"><circle cx="6" cy="3.5" r="3" fill="#fff"/><path d="M0 12c0-4 3-5 6-5s6 1 6 5z" fill="#fff"/></svg>Member Sign In</div>
  <div class="abs state-mark" aria-hidden="true"></div>
  <div class="abs tab tab-club">
    <svg width="12" height="12" viewBox="0 0 12 12"><path d="M1 6h7M5 3l3 3-3 3" stroke="#fff" stroke-width="2" fill="none"/><path d="M7 1h4v10H7" stroke="#fff" stroke-width="1.5" fill="none"/></svg>Club Sign In</div>
  <nav class="abs nav">
    <a>Home</a><a>About</a><a>How to Play</a><a>Newsletter</a><a>Clubs</a><a>Club News</a><a>Events</a><a>Results</a><a class="more">More..</a>
  </nav>

  <!-- hero -->
  <div class="abs hero" role="img" aria-label="Croquet player's feet and mallet on a lawn with coloured balls"></div>
  <div class="abs logo-disc">
    <span class="dot"></span>
    <span class="name">Marlowe Lawn Sports Guild</span>
  </div>
  <div class="abs hero-box">
    <h1 class="head hero-title">Croquet Club</h1>
    <p class="hero-sub">Sed ut perspiciatis unde omnis iste natsit voluptatem accusantium doloremque</p>
  </div>
  <a class="btn hero-join">Join a Croquet Club</a>
  <div class="abs dots"><span></span><span></span><span></span><span></span><span></span></div>
  <div class="abs notch"></div>

  <!-- about -->
  <div class="ghost" style="left:160px;top:842px;font-size:62px;line-height:1.1">About<br>Croquet Club</div>
  <h2 class="abs head about-title">About<span>Croquet Club</span></h2>
  <p class="abs about-text">Croquet is a very old game that had its beginnings in the early 1400's. Below is a brief history of the game. England developed the initial rules of the game in the mid 1800's and the game is now played in about 26 countries around the world. Australia was an early adopter of the game and now has about 8,000 players of which just under 3,000 are in NSW. Since its early beginnings, croquet has evolved into <a>5 different codes</a> and the rules formalised to provide the modern games.</p>
  <div class="abs about-frame"></div>
  <div class="abs about-photo" role="img" aria-label="Group of croquet players standing together on a club lawn"></div>
  <div class="abs play"><svg width="58" height="58" viewBox="0 0 58 58"><path d="M23 18l17 11-17 11z" fill="#fff"/></svg></div>
  <a class="btn btn-outline-green read-more">READ MORE INFO</a>

  <!-- newsletters -->
  <section class="abs news">
    <svg width="1200" height="622" style="position:absolute;left:0;top:0" aria-hidden="true">
      <polygon points="0,0 420,0 180,300" fill="#e4ecf7"/>
      <polygon points="420,0 820,0 620,260" fill="#f5f8fc"/>
      <polygon points="820,0 1200,0 1200,320" fill="#e6eef8"/>
      <polygon points="0,300 260,622 0,622" fill="#e8eff8"/>
      <polygon points="600,400 900,622 320,622" fill="#e2eaf5"/>
      <polygon points="1200,320 1200,622 960,622" fill="#f4f7fb"/>
    </svg>
  </section>
  <h2 class="head section-title" style="top:1520px">Our <span>MLSG Newsletters</span></h2>
  <p class="section-sub" style="top:1582px">Sed ut perspiciatis unde omnis iste natus error sit voluptatem accusantium doloremque laudantium explicabo.</p>

  <div class="abs nl" style="left:99px;top:1629px"><h4>MLSG NEWSLETTER</h4><p>Spring Test Series A Going for Glory</p><span class="rm">Read More &gt;&gt;</span></div>
  <div class="abs nl-date" style="left:247px;top:1774px">June<b>2018</b></div>
  <div class="abs nl" style="left:453px;top:1629px"><h4>MLSG NEWSLETTER</h4><p>State Advisory Group Classic 2018 Cup Team</p><span class="rm">Read More &gt;&gt;</span></div>
  <div class="abs nl-date" style="left:601px;top:1774px">March<b>2018</b></div>
  <div class="abs nl" style="left:806px;top:1629px"><h4>MLSG NEWSLETTER</h4><p>Club Pairs Finalists Across Regional NSW</p><span class="rm">Read More &gt;&gt;</span></div>
  <div class="abs nl-date" style="left:954px;top:1774px">December<b>2017</b></div>
  <span class="abs arrow" style="left:58px">‹</span>
  <span class="abs arrow" style="left:1124px">›</span>

  <!-- calendar & events -->
  <div class="abs cal-panel"></div>
  <h3 class="abs head cal-title">Calendar of Events</h3>
  <div class="abs cal">
    <div class="cal-head"><span>‹</span><span>JUNE 2018</span><span>›</span></div>
    <div class="cal-grid">
      <div class="wd">MON</div><div class="wd">TUE</div><div class="wd">WED</div><div class="wd">THU</div><div class="wd">FRI</div><div class="wd">SAT</div><div class="wd">SUN</div>
      <div class="mute">30</div><div>1</div><div>2</div><div>3</div><div>4</div><div>5</div><div>6</div>
      <div>7</div><div>8</div><div>9</div><div>10</div><div>11</div><div>12</div><div class="on">13</div>
      <div>14</div><div>15</div><div>16</div><div>17</div><div>18</div><div>19</div><div>20</div>
      <div>21</div><div>22</div><div>23</div><div>24</div><div>25</div><div>26</div><div>27</div>
      <div>28</div><div>29</div><div>30</div><div>31</div><div class="mute">1</div><div class="mute">2</div><div class="mute">3</div>
    </div>
  </div>
  <div class="abs cal-topics"><a>Event Topics</a><br><span style="color:#333">All Topics</span></div>

  <div class="ghost" style="left:842px;top:2100px;font-size:78px">Events</div>
  <h3 class="abs events-h" style="left:458px;top:2126px">Our Events On June 2018</h3>
  <ul class="abs ev-list" style="left:458px;top:2180px">
    <li>Sed ut perspiciatis unde omnis iste natus error sit voluptatem accusantium doloremque</li>
    <li>Usu id iudico dicant reprehendunt, modus fiererit his ei, tatus insolens nam te. Ex velit aliquip saepeit vel, duo erant commodo conclusionemque id</li>
  </ul>
  <h3 class="abs events-h" style="left:458px;top:2304px">Popular Events</h3>
  <ul class="abs ev-list" style="left:458px;top:2356px">
    <li>Usu id iudico dicant reprehendunt, modus fiererit his ei, tatus insolens nam te. Ex velit aliquip saepeit vel, duo erant commodo conclusionemque id</li>
  </ul>
  <a class="btn btn-green more-events">More Events</a>

  <!-- training -->
  <div class="abs train"></div>
  <div class="ghost" style="left:99px;top:2668px;font-size:46px;line-height:1.05;color:rgba(255,255,255,.1)">Training<br>Resources</div>
  <h2 class="abs head train-title">Training Resources</h2>
  <p class="abs train-text">Sed ut perspiciatis unde omnis iste natus error sit voluptatem accusantium doloremque laudantium, totam rem aperiam, eaque ipsa quae ab illo inventore veritatis et quasi architectoluptatecto beatae vitae dicta sunt explicaboma enim ipsam voluptateoluptateoluptateoluptateo luptatem quia voluptas sit aspernatur aut..</p>
  <a class="btn train-btn">READ MORE</a>
  <div class="abs train-photo" role="img" aria-label="Croquet players in white on a lawn during a training session"></div>

  <!-- downloads -->
  <div class="ghost" style="left:0;width:1200px;text-align:center;top:3222px;font-size:58px">Downloads</div>
  <h2 class="head section-title" style="top:3251px">Our <span>Downloads</span></h2>
  <p class="section-sub" style="top:3310px;line-height:2.1;padding:0 280px">Sed ut perspiciatis unde omnis iste natus error sit voluptatem accusantium doloremque sed quia non numquam eius modi tempora incidunt ut labore et laudantium explicabo.</p>
  <a class="btn btn-outline-green dl-btn">Download Now
    <svg width="14" height="14" viewBox="0 0 14 14"><path d="M7 1v8M3 6l4 4 4-4M1 13h12" stroke="#00a990" stroke-width="2" fill="none"/></svg></a>

  <!-- footer -->
  <footer class="abs footer"></footer>
  <div class="abs f-logo"><span class="sq"></span>Marlowe Lawn Sports Guild</div>
  <div class="abs f-call">
    <svg width="20" height="20" viewBox="0 0 24 24"><path d="M6.6 10.8a15 15 0 006.6 6.6l2.2-2.2a1 1 0 011-.25 11.4 11.4 0 003.6.6 1 1 0 011 1V20a1 1 0 01-1 1A17 17 0 013 4a1 1 0 011-1h3.5a1 1 0 011 1c0 1.25.2 2.45.6 3.6a1 1 0 01-.25 1z" fill="#fff"/></svg>
    Call us : ( 1 800 555 0142)</div>
  <p class="abs f-mid">Sed quia non numquam<br>eius modi tempora..</p>
  <a class="btn f-contact">Contact us</a>
  <h4 class="abs f-news">Sign up Newsletter</h4>
  <div class="abs f-input">Enter Email</div>
  <a class="btn f-login">LOG IN</a>
  <div class="abs f-rule"></div>
  <p class="abs f-copy">© copyright 2018 Marlowe Lawn Sports Guild.All Rights Reserved &nbsp;|&nbsp; Privacy policy &nbsp;|&nbsp; Terms and use</p>
  <div class="abs socials" aria-label="Social links">
    <span style="background:#3b5998"></span><span style="background:#1da1f2"></span><span style="background:#e62117"></span><span style="background:#0077b5"></span><span style="background:#dd4b39"></span>
  </div>
</div>
</body>
</html>
```